Sign Front of Business

Sign for front of workshop. We want KRT Mechanical in same font and colour as logo then the logo after name. Would like a background colour maybe dark blue with a border.

Target Market(s)

Mining Community

Industry/Entity Type

Mechanical

Requirements
Must have
• Logo colours

```html
<!DOCTYPE html>
<html lang="en">
<head>
<meta charset="utf-8">
<title>KRT Mechanical – Workshop Sign</title>
<link rel="stylesheet" href="https://fonts.googleapis.com/css2?family=Russo+One&display=swap">
<style>
  :root {
    --page-bg: #ffffff;
    --sign-navy: #131d4f;
    --sign-navy-deep: #0d1540;
    --accent-red: #b0161c;
    --accent-red-dark: #7e0f13;
    --accent-blue: #3d7fd6;
    --steel: #d9dde3;
    --steel-dark: #8a929c;
    --rule: #000000;
    --name-blue: #4a8fe0;
    --badge-blue: #2a5fb8;
  }
  * { margin: 0; padding: 0; box-sizing: border-box; }
  html, body {
    width: 800px; height: 1200px; overflow: hidden;
    background: var(--page-bg);
  }
  .canvas {
    position: relative; width: 800px; height: 1200px;
    display: flex; align-items: center; justify-content: center;
  }
  .sign {
    position: relative; width: 760px; height: 445px;
    background: radial-gradient(ellipse at 70% 50%, var(--sign-navy) 0%, var(--sign-navy-deep) 80%);
    overflow: hidden;
  }
  .sign-trim { position: absolute; inset: 0; width: 100%; height: 100%; }
  .business-name {
    position: absolute; left: 50px; top: 160px; width: 330px;
    font-family: "Russo One", sans-serif; color: var(--name-blue);
    text-align: center; line-height: 1;
  }
  .business-name .name-main { display: block; font-size: 92px; letter-spacing: 2px; }
  .business-name .name-sub { display: block; font-size: 33px; margin-top: 6px; letter-spacing: 1px; }
  .divider {
    position: absolute; left: 452px; top: 135px; width: 1px; height: 180px;
    background: var(--steel-dark);
  }
  .brand-mark {
    position: absolute; left: 480px; top: 95px; width: 250px; height: 255px;
    display: flex; flex-direction: column; align-items: center; justify-content: center; gap: 14px;
  }
  .brand-mark .mark-circle {
    width: 150px; height: 150px; border-radius: 50%;
    background: var(--badge-blue);
  }
  .brand-mark .mark-name {
    font-family: "Russo One", sans-serif; font-size: 24px; color: var(--name-blue);
  }
</style>
</head>
<body>
<main class="canvas">
  <section class="sign" aria-label="KRT Mechanical workshop sign">
    <svg class="sign-trim" viewBox="0 0 760 445" preserveAspectRatio="none" aria-hidden="true">
      <defs>
        <linearGradient id="redFadeTop" x1="0" x2="1" y1="0" y2="0">
          <stop offset="0" stop-color="var(--accent-red)" stop-opacity="0"/>
          <stop offset="0.45" stop-color="var(--accent-red)"/>
          <stop offset="1" stop-color="var(--accent-red-dark)"/>
        </linearGradient>
        <linearGradient id="redFadeBottom" x1="1" x2="0" y1="0" y2="0">
          <stop offset="0" stop-color="var(--accent-red)" stop-opacity="0"/>
          <stop offset="0.5" stop-color="var(--accent-red)"/>
          <stop offset="1" stop-color="var(--accent-red-dark)"/>
        </linearGradient>
        <linearGradient id="blueFade" x1="0" x2="1">
          <stop offset="0" stop-color="var(--accent-blue)"/>
          <stop offset="1" stop-color="var(--accent-blue)" stop-opacity="0"/>
        </linearGradient>
        <linearGradient id="steelLine" x1="0" x2="1">
          <stop offset="0" stop-color="var(--steel-dark)"/>
          <stop offset="0.5" stop-color="var(--steel)"/>
          <stop offset="1" stop-color="var(--steel-dark)"/>
        </linearGradient>
      </defs>
      <!-- top trim -->
      <rect class="top-rule" x="0" y="0" width="760" height="5" fill="var(--rule)"/>
      <path class="top-band" d="M0 5 H760 V45 C620 42 560 18 420 14 H0 Z" fill="url(#redFadeTop)"/>
      <path class="top-band-fill" d="M0 5 H760 V8 H0 Z" fill="var(--accent-red)"/>
      <rect class="top-blue-line" x="0" y="36" width="210" height="4" fill="url(#blueFade)"/>
      <path class="top-steel-line" d="M230 35 H560 C600 35 620 37 650 40 L650 42 C620 40 600 39 560 39 H230 Z" fill="url(#steelLine)"/>
      <!-- bottom trim -->
      <path class="bottom-band" d="M0 400 C140 402 200 428 340 432 H760 V440 H0 Z" fill="url(#redFadeBottom)"/>
      <rect class="bottom-rule" x="0" y="440" width="760" height="5" fill="var(--rule)"/>
      <rect class="bottom-blue-line" x="550" y="404" width="210" height="4" fill="url(#blueFade)" transform="rotate(180 655 406)"/>
      <path class="bottom-steel-line" d="M120 405 C160 407 180 408 210 408 H520 V412 H210 C180 412 160 410 120 407 Z" fill="url(#steelLine)"/>
    </svg>

    <h1 class="business-name">
      <span class="name-main">KRT</span>
      <span class="name-sub">MECHANICAL</span>
    </h1>

    <div class="divider"></div>

    <div class="brand-mark">
      <div class="mark-circle"></div>
      <span class="mark-name">KRT Mechanical</span>
    </div>
  </section>
</main>
</body>
</html>
```